Business Card Design Project

Business card design for an IT Service company. A logo has already been created in a different contest and has been attached to this project. Ideally we're looking for a double sided business card that matches the look and feel of our newly created logo.

We're open to creativity if you feel a tag line is needed such as "IT Services and Application Development". We're open to really and look and feel - even single sided business cards if you feel you have something that's a great idea.

Last thought here - I'm not sure how it'll look but maybe a two tone card? One side dark blue and the other side white? Don't limit the design submissions to this tho - just curious if it would look good

Nothing too busy please - simple... Thank you and happy designing!

Target Market(s)

Businesses that require IT Services and support for hosted services, technical consultation, web design.

Industry/Entity Type

Business

Font styles to use
Sans Serif

Requirements
Must have
• Use the colors provided in the logo (see attachment) or additional colors that compliment
Must have the following contact info (not necessarily in this order):
- Alan Fisk
- Founding Partner
- afisk@quillbarrow.example
- 555-382-1946
- www.quillbarrow.example

```html
<!DOCTYPE html>
<html lang="en">
<head>
<meta charset="utf-8">
<title>QuillBarrow Business Card</title>
<link rel="stylesheet" href="https://fonts.googleapis.com/css2?family=Open+Sans:wght@400;600;700&display=swap">
<style>
  :root {
    --stage: #e4e5e8;
    --navy: #33426e;
    --navy-deep: #2a3760;
    --ink: #283a66;
    --ink-soft: #4a5578;
    --paper: #ffffff;
    --accent: #7a9a3a;
  }
  * { box-sizing: border-box; margin: 0; padding: 0; }
  html, body {
    width: 1200px; height: 800px; overflow: hidden;
    background: var(--stage);
    font-family: "Open Sans", Arial, sans-serif;
  }
  .canvas {
    position: relative; width: 1200px; height: 800px;
  }
  .card {
    position: absolute; left: 337px;
    width: 525px; height: 300px;
    border-radius: 4px;
    box-shadow: 0 8px 24px rgba(30, 40, 70, 0.18);
    overflow: hidden;
  }
  .card--front { top: 70px; background: var(--paper); }
  .card--back {
    top: 430px;
    background: linear-gradient(135deg, #3d4d7c 0%, var(--navy) 45%, var(--navy-deep) 100%);
    display: flex; align-items: center; justify-content: center;
  }
  .front__brand {
    position: absolute; left: 38px; top: 30px;
    font-size: 34px; font-weight: 700; color: var(--ink);
    letter-spacing: -0.5px;
  }
  .front__person { position: absolute; left: 38px; top: 98px; }
  .person__name { font-size: 22px; font-weight: 700; color: var(--ink); line-height: 1.2; }
  .person__title { font-size: 13px; font-weight: 400; color: var(--ink-soft); }
  .contact-list {
    position: absolute; left: 38px; top: 168px;
    list-style: none;
  }
  .contact-list li {
    display: flex; align-items: center; gap: 10px;
    font-size: 13px; color: var(--ink); line-height: 26px;
  }
  .contact-list svg { width: 13px; height: 13px; flex: none; }
  .back__brand {
    display: flex; align-items: center; gap: 14px;
    font-size: 52px; font-weight: 700; color: var(--paper);
    letter-spacing: -0.5px;
  }
  .brand-square {
    width: 22px; height: 22px; background: var(--accent);
  }
</style>
</head>
<body>
<main class="canvas">
  <section class="card card--front" aria-label="Card front">
    <div class="front__brand">QuillBarrow</div>
    <div class="front__person">
      <p class="person__name">Alan Fisk</p>
      <p class="person__title">Founding Partner</p>
    </div>
    <ul class="contact-list">
      <li>
        <svg viewBox="0 0 16 16" aria-hidden="true"><path fill="#283a66" d="M3.6 1.2l2.3 2.6-1.4 1.8c.9 2 2.5 3.6 4.5 4.5l1.8-1.4 2.6 2.3-1.3 2.2C7 13.4 2.6 9 1.4 2.5z"/></svg>
        555-382-1946
      </li>
      <li>
        <svg viewBox="0 0 16 16" aria-hidden="true"><rect x="1" y="3" width="14" height="10" fill="none" stroke="#283a66" stroke-width="1.5"/><path d="M1 3.5l7 5.5 7-5.5" fill="none" stroke="#283a66" stroke-width="1.5"/></svg>
        afisk@quillbarrow.example
      </li>
      <li>
        <svg viewBox="0 0 16 16" aria-hidden="true"><g fill="none" stroke="#283a66" stroke-width="1.3"><circle cx="8" cy="8" r="6.5"/><ellipse cx="8" cy="8" rx="2.8" ry="6.5"/><path d="M1.5 8h13M2.5 4.8h11M2.5 11.2h11"/></g></svg>
        www.quillbarrow.example
      </li>
    </ul>
  </section>

  <section class="card card--back" aria-label="Card back">
    <div class="back__brand"><span class="brand-square"></span>QuillBarrow</div>
  </section>
</main>
</body>
</html>
```